Ninety Truths Earned Across Four Decades of Advisory Work

I need the design for my book cover, plus the spine and the back cover. I need this for both a hard cover book and an ebook

Target Market(s)

Any person in business with managerial responsibility

Industry/Entity Type

Consulting

Font styles to use
Serif

Requirements
Must have
• Must look very professional. No script/cursive is to be used. The cover should be clean, not cluttered.so the title really stands out well
Nice to have
• A professional image to reinforce the title
Should not have
• Script, cartoons or anything that does not look professional

```html
<!DOCTYPE html>
<html lang="en">
<head>
<meta charset="utf-8">
<title>Ninety Truths Earned Across Four Decades of Advisory Work</title>
<link rel="stylesheet" href="https://fonts.googleapis.com/css2?family=Raleway:wght@800;900&display=swap">
<style>
  :root {
    --page-bg: #dfe4e8;
    --cover-top: #c2c2c2;
    --cover-mid: #e4e4e4;
    --cover-bottom: #fafafa;
    --title-red: #a3202f;
    --band-grey: #a6a6a6;
    --ink: #141414;
    --art-dark: #bdbdbd;
    --art-light: #ececec;
  }
  * { margin: 0; padding: 0; box-sizing: border-box; }
  html, body {
    width: 1200px;
    height: 848px;
    overflow: hidden;
    background: var(--page-bg);
    font-family: "Raleway", sans-serif;
  }
  .canvas {
    width: 1200px;
    height: 848px;
    display: flex;
    align-items: center;
    justify-content: center;
  }
  .cover {
    position: relative;
    width: 560px;
    height: 810px;
    background: linear-gradient(165deg, var(--cover-top) 0%, var(--cover-mid) 40%, var(--cover-bottom) 80%);
    overflow: hidden;
  }
  .title-block {
    position: absolute;
    top: 78px;
    left: 0;
    right: 0;
    display: flex;
    flex-direction: column;
    align-items: center;
    font-weight: 900;
  }
  .title-word {
    display: block;
    color: var(--title-red);
    font-weight: 900;
    line-height: 0.8;
    letter-spacing: -3px;
  }
  .title-word--first { font-size: 112px; }
  .title-word--second { font-size: 176px; margin-top: 2px; }
  .title-band {
    position: relative;
    z-index: 2;
    display: block;
    background: var(--band-grey);
    color: var(--ink);
    font-weight: 800;
    font-size: 24px;
    line-height: 1;
    padding: 5px 10px 4px;
    text-transform: uppercase;
    white-space: nowrap;
  }
  .title-band--first { margin-top: -14px; }
  .title-band--second { margin-top: -22px; }
  .cover-art {
    position: absolute;
    left: 30px;
    right: 30px;
    top: 430px;
    bottom: 0;
    border-radius: 250px 250px 0 0;
    background: linear-gradient(180deg, var(--art-dark) 0%, var(--art-light) 55%, var(--cover-bottom) 100%);
    opacity: 0.75;
  }
  .author {
    position: absolute;
    left: 0;
    right: 0;
    bottom: 100px;
    text-align: center;
    color: var(--ink);
    font-weight: 900;
    font-size: 52px;
    letter-spacing: 1px;
    text-transform: uppercase;
  }
</style>
</head>
<body>
  <main class="canvas">
    <section class="cover">
      <div class="cover-art" role="img" aria-label="Sketched illustration of a person with a megaphone sending communication icons in a dashed arc to a seated person with a laptop, above a faint crowd of people"></div>
      <h1 class="title-block">
        <span class="title-word title-word--first">NINETY</span>
        <span class="title-band title-band--first">Truths Earned Across</span>
        <span class="title-word title-word--second">FOUR</span>
        <span class="title-band title-band--second">Decades of Advisory Work</span>
      </h1>
      <p class="author">Lorem Ipsum</p>
    </section>
  </main>
</body>
</html>
```